iOS7 test prep app

I need 3 basic screens and 2 product images for an iOS7 app I am prototyping. I provided lots of detail in the attached brief. This is an education product, so warm colors (especially reds) work best.

If you've done flat design for mobile products, please take a look ... Thanks!

Greetings, all. Thank you for your submissions. I am meeting with my product development team this week to review your submissions, and will select a designer before the end of the week. I appreciate your patience with my process, and thank you again for your interest in my project. I'll be back to you soon ... -Dorian

```html
<!DOCTYPE html>
<html lang="en">
<head>
<meta charset="utf-8">
<title>Test Prep App – Question Screens</title>
<link href="https://fonts.googleapis.com/css2?family=Arimo:wght@400;700&display=swap" rel="stylesheet">
<style>
  :root {
    --canvas: #e4e4e4;
    --screen: #1c1c1c;
    --card: #2a2a2a;
    --card-edge: #333333;
    --pill: #3a3a3a;
    --brand-red: #e05848;
    --button-red: #c8392e;
    --brand-green: #1b8a4c;
    --answer-green: #2fae5e;
    --text: #f2f2f2;
    --muted: #7a7a7a;
    --highlight: #4a4a4a;
    --track: #3c3c3c;
  }
  * { box-sizing: border-box; margin: 0; padding: 0; }
  html, body {
    width: 1200px; height: 1000px; overflow: hidden;
    background: var(--canvas);
    font-family: "Arimo", "Helvetica Neue", Arial, sans-serif;
    color: var(--text);
  }
  .stage {
    position: relative; width: 1200px; height: 1000px;
    display: flex; justify-content: center; align-items: center; gap: 70px;
  }
  .screen {
    width: 360px; height: 680px;
    background: var(--screen);
    display: flex; flex-direction: column;
    box-shadow: 0 10px 30px rgba(0,0,0,.18);
  }
  .app-bar { background: var(--brand-red); color: #fff; }
  .status-bar {
    height: 24px; padding: 0 8px;
    display: flex; align-items: center; justify-content: space-between;
    font-size: 13px;
  }
  .status-left, .status-right { display: flex; align-items: center; gap: 5px; }
  .status-time { font-weight: 700; font-size: 14px; }
  .title-bar {
    height: 48px; position: relative;
    display: flex; align-items: center; justify-content: center;
    font-size: 17px; font-weight: 700;
  }
  .menu-icon { position: absolute; left: 16px; top: 16px; }
  .content { flex: 1; padding: 12px 10px 14px; display: flex; flex-direction: column; gap: 14px; }
  .card {
    background: var(--card); border: 1px solid var(--card-edge);
    border-radius: 3px; padding: 8px 0 10px;
  }
  .pill {
    display: inline-flex; align-items: center; gap: 14px;
    margin-left: 8px; padding: 3px 30px 3px 4px;
    background: var(--pill); border-radius: 14px;
    font-size: 15px;
  }
  .pill-icon {
    width: 20px; height: 20px; border-radius: 50%;
    background: #8a8a8a; color: #2a2a2a;
    display: flex; align-items: center; justify-content: center;
    font-size: 13px; font-weight: 700;
  }
  .pill-question { color: var(--brand-red); }
  .pill-answer { color: var(--answer-green); }
  .question-text { padding: 8px 12px 10px; font-size: 15.5px; line-height: 1.22; }
  .options { list-style: none; border-top: 1px solid #3a3a3a; padding-top: 6px; }
  .option { padding: 4px 12px; font-size: 15.5px; }
  .option.is-selected { background: var(--highlight); }
  .options.is-revealed .option { color: var(--muted); }
  .options.is-revealed .option.is-correct { color: var(--answer-green); }
  .answer-text { padding: 10px 12px 2px; font-size: 14.5px; line-height: 1.22; }
  .confidence {
    margin-top: 18px; background: var(--card); border-radius: 3px;
    height: 54px; display: flex; align-items: center; justify-content: center;
    font-size: 19px;
  }
  .slider { position: relative; height: 70px; margin: 0 16px; }
  .slider-track { position: absolute; left: 12px; right: 0; top: 52px; height: 3px; background: var(--track); }
  .slider-fill { position: absolute; left: 12px; width: 40%; top: 52px; height: 3px; background: var(--brand-green); }
  .slider-dots { position: absolute; left: 12px; right: 0; top: 51px; display: flex; justify-content: space-between; }
  .slider-dots span { width: 5px; height: 5px; border-radius: 50%; background: #fff; }
  .slider-pin { position: absolute; left: 132px; top: 10px; }
  .button {
    height: 52px; border-radius: 2px; color: #fff;
    display: flex; align-items: center; justify-content: center; font-size: 18px;
  }
  .button-green { background: var(--brand-green); }
  .button-red { background: var(--button-red); }
  .spacer { flex: 1; }
  .button-row { display: flex; gap: 10px; }
  .button-row .button { flex: 1; }
</style>
</head>
<body>
<main class="stage">

  <section class="screen">
    <header class="app-bar">
      <div class="status-bar">
        <div class="status-left">
          <svg width="26" height="6" viewBox="0 0 26 6"><g fill="#fff"><circle cx="3" cy="3" r="2.5"/><circle cx="8" cy="3" r="2.5"/><circle cx="13" cy="3" r="2.5"/></g><g fill="none" stroke="#fff"><circle cx="18" cy="3" r="2.2"/><circle cx="23" cy="3" r="2.2"/></g></svg>
          <span>VELA</span>
          <svg width="14" height="10" viewBox="0 0 14 10"><path d="M1 3.5a9 9 0 0 1 12 0M3.3 5.8a5.6 5.6 0 0 1 7.4 0M5.6 8a2.2 2.2 0 0 1 2.8 0" fill="none" stroke="#fff" stroke-width="1.4"/></svg>
        </div>
        <span class="status-time">4:21 PM</span>
        <div class="status-right">
          <svg width="8" height="12" viewBox="0 0 8 12"><path d="M1 3l6 5-3 3V1l3 3-6 5" fill="none" stroke="#fff" stroke-width="1.2"/></svg>
          <span>100%</span>
          <svg width="24" height="11" viewBox="0 0 24 11"><rect x="0.5" y="0.5" width="20" height="10" rx="2" fill="none" stroke="#fff"/><rect x="2" y="2" width="17" height="7" fill="#fff"/><rect x="21.5" y="3.5" width="2" height="4" fill="#fff"/></svg>
        </div>
      </div>
      <div class="title-bar">
        <svg class="menu-icon" width="20" height="15" viewBox="0 0 20 15"><g fill="#fff"><rect width="20" height="2.5"/><rect y="6" width="20" height="2.5"/><rect y="12" width="20" height="2.5"/></g></svg>
        Question 7 of 100
      </div>
    </header>
    <div class="content">
      <article class="card">
        <span class="pill"><span class="pill-icon">?</span><span class="pill-question">Questions</span></span>
        <p class="question-text">A patient presents to the emergency room with the following symptoms: Anxiety, dyspnea, rhonchi, fever, Oxygen saturation of 88%, and a pH of 7.21. The nurse realized that the patient suffering from:</p>
        <ul class="options">
          <li class="option">A. Respiratory alkalosis</li>
          <li class="option">B. Metabolic alkalosis</li>
          <li class="option is-selected">C. Respiratory acidosis</li>
          <li class="option">D. Metabolic acidosis</li>
        </ul>
      </article>
      <div>
        <div class="confidence">Confidence</div>
        <div class="slider">
          <div class="slider-track"></div>
          <div class="slider-fill"></div>
          <div class="slider-dots"><span></span><span></span><span></span><span></span><span></span><span></span><span></span><span></span><span></span><span></span></div>
          <svg class="slider-pin" width="36" height="44" viewBox="0 0 36 44">
            <path d="M18 42 C10 32 2 26 2 18 a16 16 0 0 1 32 0 c0 8-8 14-16 24z" fill="var(--brand-green)"/>
            <text x="18" y="22" text-anchor="middle" font-size="11" fill="#fff" font-family="Arimo, sans-serif">50</text>
          </svg>
        </div>
      </div>
      <div class="spacer"></div>
      <div class="button button-green">Submit</div>
    </div>
  </section>

  <section class="screen">
    <header class="app-bar">
      <div class="status-bar">
        <div class="status-left">
          <svg width="26" height="6" viewBox="0 0 26 6"><g fill="#fff"><circle cx="3" cy="3" r="2.5"/><circle cx="8" cy="3" r="2.5"/><circle cx="13" cy="3" r="2.5"/></g><g fill="none" stroke="#fff"><circle cx="18" cy="3" r="2.2"/><circle cx="23" cy="3" r="2.2"/></g></svg>
          <span>VELA</span>
          <svg width="14" height="10" viewBox="0 0 14 10"><path d="M1 3.5a9 9 0 0 1 12 0M3.3 5.8a5.6 5.6 0 0 1 7.4 0M5.6 8a2.2 2.2 0 0 1 2.8 0" fill="none" stroke="#fff" stroke-width="1.4"/></svg>
        </div>
        <span class="status-time">4:21 PM</span>
        <div class="status-right">
          <svg width="8" height="12" viewBox="0 0 8 12"><path d="M1 3l6 5-3 3V1l3 3-6 5" fill="none" stroke="#fff" stroke-width="1.2"/></svg>
          <span>100%</span>
          <svg width="24" height="11" viewBox="0 0 24 11"><rect x="0.5" y="0.5" width="20" height="10" rx="2" fill="none" stroke="#fff"/><rect x="2" y="2" width="17" height="7" fill="#fff"/><rect x="21.5" y="3.5" width="2" height="4" fill="#fff"/></svg>
        </div>
      </div>
      <div class="title-bar">
        <svg class="menu-icon" width="20" height="15" viewBox="0 0 20 15"><g fill="#fff"><rect width="20" height="2.5"/><rect y="6" width="20" height="2.5"/><rect y="12" width="20" height="2.5"/></g></svg>
        Question 7 of 100
      </div>
    </header>
    <div class="content">
      <article class="card">
        <span class="pill"><span class="pill-icon">?</span><span class="pill-question">Questions</span></span>
        <p class="question-text">A patient presents to the emergency room with the following symptoms: Anxiety, dyspnea, rhonchi, fever, Oxygen saturation of 88%, and a pH of 7.21. The nurse realized that the patient suffering from:</p>
        <ul class="options is-revealed">
          <li class="option">A. Respiratory alkalosis</li>
          <li class="option">B. Metabolic alkalosis</li>
          <li class="option is-correct">C. Respiratory acidosis</li>
          <li class="option">D. Metabolic acidosis</li>
        </ul>
      </article>
      <article class="card">
        <span class="pill"><span class="pill-icon">!</span><span class="pill-answer">Answer</span></span>
        <p class="answer-text">The correct answer is C.<br>A key symptom of respiratory distress syndrome is the inability of the respiratory system to exchange gases, resulting in respiratory acidosis.</p>
      </article>
      <div class="spacer"></div>
      <div class="button-row">
        <div class="button button-red">Save &amp; Close</div>
        <div class="button button-green">Next Question</div>
      </div>
    </div>
  </section>

</main>
</body>
</html>
```